Managed Service Provider need new business cards

We are a small Maanged Service Provider of IT Services and need a new fresh design for our business cards. We want something impossible, fun and professional :)
Our services has a large range, but we are always fun and make sure our customers both get their issue sorted and also feel like they are "catching up with an old friend".
All our cards in the past has always been all black, with red and we need something fresher.
The back of card, we would like just a small list of what we do i think, but if someone has a better idea, please do something cool with the back of the card:
Managed IT Services
Productivity Solutions
Data Backup and Recovery
IT System Maintenance
Managed IT Security
More details can be found on our website tqnetworks.com.au
Industry/Entity Type
It Company
Contact Information for Business Card
Name: Dwayne Falstrup
Title: Director
Phone: 03 6193 4827
Mobile: 0412 587 239
Email: dwayne@tqnetworks.com.au
Web: www.tqnetworks.com.au

```html
<!DOCTYPE html>
<html lang="en">
<head>
<meta charset="utf-8">
<title>TQ Networks — Business Card</title>
<link rel="stylesheet" href="https://fonts.googleapis.com/css2?family=Lexend:wght@400;500;700&display=swap">
<style>
  :root {
    --brand-red: #ee1c1c;
    --brand-red-deep: #d40d0d;
    --ink: #111111;
    --paper: #f4f4f4;
    --paper-shade: #e6e6e6;
    --stage: #e4e6e8;
    --white: #ffffff;
  }
  * { box-sizing: border-box; margin: 0; padding: 0; }
  html, body { width: 1141px; height: 1200px; overflow: hidden; }
  body {
    background: var(--stage);
    font-family: "Lexend", Arial, sans-serif;
    color: var(--ink);
    position: relative;
  }
  .card {
    position: absolute;
    left: 143px;
    width: 824px;
    background: linear-gradient(135deg, var(--paper) 0%, var(--white) 45%, var(--paper-shade) 100%);
    box-shadow: 0 4px 14px rgba(0,0,0,0.18);
    overflow: hidden;
  }
  .card--front { top: 68px; height: 471px; }
  .card--back { top: 582px; height: 478px; }

  /* Front */
  .front-panel {
    position: absolute; left: 0; top: 0; width: 382px; height: 100%;
    background: linear-gradient(160deg, var(--brand-red) 0%, var(--brand-red-deep) 100%);
    overflow: hidden;
  }
  .brand-name {
    font-weight: 700;
    color: var(--white);
    letter-spacing: 0.5px;
    white-space: nowrap;
  }
  .front-panel .brand-name {
    position: absolute; left: 50px; top: 44px; font-size: 33px; line-height: 40px;
  }
  .illustration {
    position: absolute; left: 29px; top: 239px; width: 320px; height: 147px;
    border-radius: 6px;
    background: linear-gradient(180deg, #8a8f96 0%, #4b5058 70%, #2a2d33 100%);
  }
  .identity { position: absolute; left: 382px; right: 0; top: 0; text-align: center; }
  .identity__name { margin-top: 34px; font-size: 43px; font-weight: 700; }
  .identity__title { margin-top: 10px; font-size: 31px; font-weight: 400; }

  .contacts { position: absolute; left: 362px; top: 202px; list-style: none; }
  .contacts li {
    display: flex; align-items: center; height: 38px; margin-bottom: 22px;
    font-size: 27px; letter-spacing: 0.3px;
  }
  .contact-icon {
    width: 38px; height: 38px; border-radius: 50%; background: var(--ink);
    display: flex; align-items: center; justify-content: center;
    margin-right: 16px; flex-shrink: 0;
  }

  /* Back */
  .back-tab {
    position: absolute; left: 268px; top: 0; width: 290px; height: 38px;
    background: var(--brand-red); border-radius: 0 0 8px 8px;
  }
  .card--back .brand-name {
    position: absolute; left: 0; right: 0; top: 58px; text-align: center;
    color: var(--brand-red); font-size: 28px; line-height: 34px;
  }
  .service {
    position: absolute; width: 260px; text-align: center;
    font-size: 21px; line-height: 29px; transform: translateX(-50%);
  }
  .service__icon {
    width: 71px; height: 71px; border-radius: 50%; background: var(--ink);
    margin: 0 auto 16px; display: flex; align-items: center; justify-content: center;
  }
  .back-url {
    position: absolute; left: 0; right: 0; top: 414px; text-align: center;
    color: var(--brand-red); font-size: 21px; letter-spacing: 0.3px;
  }
</style>
</head>
<body>

<section class="card card--front">
  <div class="front-panel">
    <div class="brand-name">TQ NETWORKS</div>
    <div class="illustration" role="img" aria-label="Illustration of technicians servicing server racks"></div>
  </div>

  <div class="identity">
    <h1 class="identity__name">Dwayne Falstrup</h1>
    <p class="identity__title">Director</p>
  </div>

  <ul class="contacts">
    <li>
      <span class="contact-icon">
        <svg width="20" height="20" viewBox="0 0 24 24"><path fill="#fff" d="M6.6 10.8a15 15 0 0 0 6.6 6.6l2.2-2.2c.3-.3.7-.4 1-.2 1.1.4 2.3.6 3.6.6.6 0 1 .4 1 1V20c0 .6-.4 1-1 1A17 17 0 0 1 3 4c0-.6.4-1 1-1h3.5c.6 0 1 .4 1 1 0 1.3.2 2.5.6 3.6.1.3 0 .7-.2 1z"/></svg>
      </span>03 6193 4827
    </li>
    <li>
      <span class="contact-icon">
        <svg width="20" height="20" viewBox="0 0 24 24"><path fill="#fff" d="M6.6 10.8a15 15 0 0 0 6.6 6.6l2.2-2.2c.3-.3.7-.4 1-.2 1.1.4 2.3.6 3.6.6.6 0 1 .4 1 1V20c0 .6-.4 1-1 1A17 17 0 0 1 3 4c0-.6.4-1 1-1h3.5c.6 0 1 .4 1 1 0 1.3.2 2.5.6 3.6.1.3 0 .7-.2 1z"/></svg>
      </span>0412 587 239
    </li>
    <li>
      <span class="contact-icon">
        <svg width="20" height="16" viewBox="0 0 24 18"><rect x="1" y="1" width="22" height="16" fill="none" stroke="#fff" stroke-width="2"/><path d="M1 1l11 9 11-9" fill="none" stroke="#fff" stroke-width="2"/></svg>
      </span>dwayne@tqnetworks.com.au
    </li>
    <li>
      <span class="contact-icon">
        <svg width="22" height="22" viewBox="0 0 24 24" fill="none" stroke="#fff" stroke-width="1.6"><circle cx="12" cy="12" r="10"/><ellipse cx="12" cy="12" rx="4.5" ry="10"/><path d="M2 12h20M4 6.5h16M4 17.5h16"/></svg>
      </span>www.tqnetworks.com.au
    </li>
  </ul>
</section>

<section class="card card--back">
  <div class="back-tab"></div>
  <div class="brand-name">TQ NETWORKS</div>

  <div class="service" style="left:185px; top:128px;">
    <div class="service__icon">
      <svg width="36" height="36" viewBox="0 0 24 24" fill="none" stroke="#fff" stroke-width="1.4"><rect x="3" y="4" width="18" height="12" rx="1"/><path d="M9 20h6M12 16v4"/><path d="M8 10l3 3 5-5"/></svg>
    </div>
    Managed IT<br>Services
  </div>

  <div class="service" style="left:397px; top:128px;">
    <div class="service__icon">
      <svg width="36" height="36" viewBox="0 0 24 24" fill="none" stroke="#fff" stroke-width="1.4"><circle cx="12" cy="10" r="3"/><path d="M12 3v2M12 15v2M5 10h2M17 10h2M7 5l1.4 1.4M15.6 13.6L17 15M7 15l1.4-1.4M15.6 6.4L17 5"/><rect x="4" y="19" width="16" height="3" rx="1"/></svg>
    </div>
    Productivity<br>Solutions
  </div>

  <div class="service" style="left:613px; top:128px;">
    <div class="service__icon">
      <svg width="36" height="36" viewBox="0 0 24 24" fill="none" stroke="#fff" stroke-width="1.4"><rect x="4" y="3" width="12" height="5" rx="1"/><rect x="4" y="9.5" width="12" height="5" rx="1"/><rect x="4" y="16" width="12" height="5" rx="1"/><circle cx="18" cy="16" r="3.5"/><path d="M20.5 18.5L22 20"/></svg>
    </div>
    Data Backup<br>&amp; Recovery
  </div>

  <div class="service" style="left:268px; top:281px;">
    <div class="service__icon">
      <svg width="36" height="36" viewBox="0 0 24 24" fill="none" stroke="#fff" stroke-width="1.4"><path d="M14.5 4a4 4 0 0 0-4.8 5.2L3.5 15.4a1.5 1.5 0 0 0 2.1 2.1l6.2-6.2A4 4 0 0 0 17 6.5l-2.3 2.3-2-.5-.5-2z"/><path d="M14 16h7M14 19h7"/></svg>
    </div>
    IT System Maintenance
  </div>

  <div class="service" style="left:570px; top:281px;">
    <div class="service__icon">
      <svg width="36" height="36" viewBox="0 0 24 24" fill="none" stroke="#fff" stroke-width="1.4"><path d="M12 2l8 3v6c0 5-3.5 9-8 11-4.5-2-8-6-8-11V5z"/><rect x="9" y="11" width="6" height="5" rx="0.5"/><path d="M10 11V9.5a2 2 0 0 1 4 0V11"/></svg>
    </div>
    Managed IT Security
  </div>

  <div class="back-url">www.tqnetworks.com.au</div>
</section>

</body>
</html>
```